Corporate Branded Documents - IT Provider - On-going work

Hi, I'm Neil a Director of Harbourline Tech Care a UK Based IT & Telecoms support firm. We've been trading for 12 years now and feel its time for a lick of paint. We have a logo, website etc but would like someone to create some standard documents for us.

- A PDF Proposal Template - We currently don't send our customers proposals as we have nothing that looks good.
- A Quote Template PDF - Example Attached
- A Order Template PDF - Example Attached
- A Invoice Template PDF - Example Attached
- A Generic Document PDF - Something we can use for customer application forms, NDA Agreements, Terms & Conditions etc

Our website can be found at www.harbourlinetechcare.co.uk - here you'll get a feel for our branding. I've also attached 2 example documents - as well as our currently used documents. Hopefully you guys can see why it needs improving.

We'd also like to work with someone long term, these documents are a start but we'd like to make sure all the work we do looks and feels as smart as possible, so there is plenty of additional work available.

None of these templates need to be Print ready, 99% of the time it will be viewed digitally, so high resolution designs are best

Thanks,

Neil

Target Market(s)

Corporate & Educational Customers

Industry/Entity Type

It Support

Font styles to use
Sans Serif

Colors
ec1f27
0692cd
ffffff

```html
<!DOCTYPE html>
<html lang="en">
<head>
<meta charset="utf-8">
<title>Harbourline Tech Care – Document Page</title>
<link href="https://fonts.googleapis.com/css2?family=Carlito:ital,wght@0,400;0,700;1,400&display=swap" rel="stylesheet">
<style>
  :root {
    --brand-red: #d71920;
    --brand-blue: #3aa0c8;
    --panel-blue: #35a3c1;
    --footer-teal: #00728f;
    --text-grey: #4a4a4a;
    --white: #ffffff;
  }
  * { margin: 0; padding: 0; box-sizing: border-box; }
  html, body { width: 851px; height: 1200px; overflow: hidden; background: var(--white); }
  body { font-family: "Carlito", "Calibri", sans-serif; position: relative; }

  .header-bar {
    position: absolute; left: 0; top: 22px; width: 653px; height: 23px;
    background: var(--brand-red);
  }
  .brand {
    position: absolute; left: 668px; top: 17px;
    display: flex; align-items: center; gap: 8px;
  }
  .brand-mark { width: 26px; height: 26px; background: var(--brand-red); }
  .brand-name {
    color: var(--footer-teal); font-weight: 700; font-size: 21px; line-height: 22px;
  }

  .pull-quote {
    position: absolute; left: 13px; top: 372px; width: 339px; height: 687px;
    background: var(--panel-blue);
    color: var(--white); font-style: italic; font-size: 19.5px; line-height: 38.4px;
    text-align: center; padding-top: 69px;
  }

  .content {
    position: absolute; left: 392px; top: 129px; width: 429px;
    color: var(--text-grey);
  }
  .subtitle {
    color: var(--brand-blue); font-weight: 700; font-size: 23px; line-height: 30px;
    margin-bottom: 2px;
  }
  .content p {
    font-size: 18.2px; line-height: 31.7px; text-align: justify;
    margin-bottom: 31.7px;
  }

  .footer-band {
    position: absolute; left: 0; top: 1158px; width: 673px; height: 42px;
    background: var(--footer-teal);
  }
  .footer-meta {
    position: absolute; left: 685px; top: 1160px; height: 36px;
    display: flex; align-items: center; font-size: 19px; color: var(--text-grey);
  }
  .footer-meta .divider { width: 1px; height: 34px; background: var(--text-grey); margin: 0 12px 0 10px; }
  .footer-meta .page-number { font-weight: 700; font-size: 21px; color: #333; }
</style>
</head>
<body>
  <div class="header-bar"></div>
  <div class="brand">
    <span class="brand-mark"></span>
    <span class="brand-name">Harbourline<br>Tech Care</span>
  </div>

  <aside class="pull-quote">
    Lorem Ipsum is simply dummy<br>
    text of the printing and<br>
    typesetting industry. Lorem Ipsum<br>
    has been the industry's industry.<br>
    Lorem Ipsum has been the<br>
    finishLorem Ipsum is simply<br>
    dummy text of the printing and<br>
    typesetting industry. Lorem Ipsum<br>
    has been the industry's industry.<br>
    Lorem Ipsum is simply dummy<br>
    text of the printing and<br>
    typesetting industry. Lorem Ipsum<br>
    has been the industry's industry.
  </aside>

  <main class="content">
    <h2 class="subtitle">Subtitle Here</h2>
    <p>Lorem Ipsum is simply dummy text of the printing and typesetting industry. Lorem Ipsum has been the industry's industry. Lorem Ipsum has been the finishLorem Ipsum is simply dummy text of the printing and typesetting industry. Lorem Ipsum has been the industry's industry. Lorem Ipsum has been the finishLorem Ipsum is simply dummy text of the printing and typesetting industry. Lorem Ipsum has been the industry's industry. Lorem Ipsum has been the finishLorem Ipsum is simply dummy text of the printing and typesetting industry. Lorem Ipsum has been the industry's industry. Lorem Ipsum has been the finish.</p>
    <p>Lorem Ipsum is simply dummy text of the printing and typesetting industry. Lorem Ipsum has been the industry's industry. Lorem Ipsum has been the finishLorem Ipsum is simply dummy text of the printing and typesetting industry. Lorem Ipsum has been the industry's industry. Lorem Ipsum has been the finishLorem Ipsum is simply dummy text of the printing and typesetting industry. Lorem Ipsum has been the industry's industry. Lorem Ipsum has been the finishLorem Ipsum is simply dummy text of the printing and typesetting industry. Lorem Ipsum has been the industry's industry. Lorem Ipsum has been the finish.</p>
  </main>

  <footer>
    <div class="footer-band"></div>
    <div class="footer-meta">
      <span class="label">Confendtial</span>
      <span class="divider"></span>
      <span class="page-number">2</span>
    </div>
  </footer>
</body>
</html>
```